Welding Fabrication and Inspection Business Card Design

Welding Fabrication and Inspection Services,

Business

Industrial Machinery ServicesMohammed Rahim30 Ballarat Street, Mount Gravatt East.4122.QLD

```html
<!DOCTYPE html>
<html lang="en">
<head>
<meta charset="UTF-8">
<title>Tarnwell Forge Services – Business Card</title>
<link rel="stylesheet" href="https://fonts.googleapis.com/css2?family=Montserrat:wght@300;400;600;700&display=swap">
<style>
  :root {
    --ink: #2b2a2a;
    --paper: #f7f7f5;
    --backdrop: #e4e2de;
    --rule: #3a3a3a;
  }
  * { box-sizing: border-box; margin: 0; padding: 0; }
  html, body {
    width: 1200px; height: 775px; overflow: hidden;
    background: var(--backdrop);
    font-family: "Montserrat", sans-serif;
  }
  .stage {
    width: 1200px; height: 775px;
    display: flex; align-items: center; justify-content: center;
  }
  .card {
    width: 400px; height: 660px;
    background: var(--paper);
    padding: 22px;
    box-shadow: 0 6px 18px rgba(0,0,0,0.15);
  }
  .card-frame {
    width: 100%; height: 100%;
    border: 2px solid var(--ink);
    display: flex; flex-direction: column;
  }
  .name-band {
    background: var(--ink);
    color: #fff;
    height: 112px;
    display: flex; flex-direction: column;
    align-items: center; justify-content: center;
    gap: 4px;
  }
  .person-name {
    font-weight: 600; font-size: 20px; letter-spacing: 0.5px;
    text-transform: uppercase;
  }
  .person-title {
    font-weight: 400; font-size: 10px; letter-spacing: 1px;
    text-transform: uppercase; color: #d8d8d8;
  }
  .brand {
    flex: 1;
    display: flex; align-items: center; justify-content: center;
    gap: 10px;
  }
  .brand-dot {
    width: 12px; height: 12px; border-radius: 50%;
    background: var(--ink);
  }
  .brand-name {
    font-weight: 700; font-size: 19px; color: var(--ink);
  }
  .contact {
    border-top: 2px solid var(--rule);
  }
  .phone {
    text-align: center;
    font-weight: 300; font-size: 20px; letter-spacing: 1px;
    color: var(--ink);
    padding: 8px 0 6px;
  }
  .contact-band {
    background: var(--ink);
    padding: 8px 0 0;
  }
  .email {
    background: var(--paper);
    border-top: 2px solid var(--rule);
    border-bottom: 2px solid var(--rule);
    text-align: center;
    font-weight: 300; font-size: 18px; letter-spacing: 1px;
    color: var(--ink);
    padding: 4px 0;
  }
  .address {
    color: #e9e9e9;
    text-align: center;
    font-weight: 300; font-size: 14px; letter-spacing: 2.5px;
    text-transform: uppercase; line-height: 1.45;
    padding: 10px 0 14px;
  }
</style>
</head>
<body>
  <main class="stage">
    <article class="card">
      <div class="card-frame">
        <header class="name-band">
          <p class="person-name">Khalid Nasser</p>
          <p class="person-title">Title</p>
        </header>
        <section class="brand">
          <span class="brand-dot"></span>
          <span class="brand-name">Tarnwell Forge Services</span>
        </section>
        <footer class="contact">
          <p class="phone">07 3318 4206</p>
          <div class="contact-band">
            <p class="email">khalid@tarnwellforge.com</p>
            <p class="address">17 Corrowen Street<br>Harlow Vale East. 4190.QLD</p>
          </div>
        </footer>
      </div>
    </article>
  </main>
</body>
</html>
```